Harbor Emberlight - Woodwick candles needing a sylish box designed

We need a box designed for our woodwick candles.
I would like to see a box that looks very stylish and I would like the logo to be in a silver foil outlined box (I will include photos of examples). I like a box that has a silver foil edge around it, though not essential. A pattern of some sort would be nice on the box, staying with the wood/beach theme. I will also need to include other information on the back of the box about the candle (can I do this after I see the design?). I need to be able to change the fragrance when needed on the box label. The box size is L105mm W105mm H128mm. I am really open to any ideas. Looking for something very stylish and luxurious looking.
The lids on my candles are silver and the candles have a wooden wick.

Target Market(s)

Department stores and retail shops

Industry/Entity Type

Retail

Colors
ffffff

Requirements
Must have
• Looking for something very stylish and luxurious looking, that will look and fit great in any large department store.
Nice to have
• Wooden look, if possible.
• Clean and crisp look. Very pretty.

```html
<!DOCTYPE html>
<html lang="en">
<head>
<meta charset="utf-8">
<title>Harbor Emberlight – Candle Box Dieline</title>
<link rel="stylesheet" href="https://fonts.googleapis.com/css2?family=Cinzel:wght@400;500&display=swap">
<style>
  :root {
    --page-bg: #eef0f1;
    --wood: #43271a;
    --wood-dark: #36200f;
    --wood-light: #52301f;
    --silver-light: #ececec;
    --silver-mid: #b9b9b9;
    --silver-dark: #8f8f8f;
    --label-ink: #ececec;
  }
  html, body {
    margin: 0;
    padding: 0;
    width: 1200px;
    height: 1000px;
    overflow: hidden;
    background: var(--page-bg);
  }
  .dieline {
    display: block;
    width: 1200px;
    height: 1000px;
  }
  .wood-face { fill: url(#woodTone); }
  .flap { fill: url(#woodTone); }
  .silver-band { fill: url(#silverSheen); }
  .label-frame { fill: none; stroke: var(--label-ink); stroke-width: 1.4; }
  .label-corner { fill: none; stroke: var(--label-ink); stroke-width: 1.2; }
  .label-rule { stroke: var(--label-ink); stroke-width: 1; }
  .brand-name, .fragrance, .back-title, .back-copy {
    font-family: "Cinzel", "Trajan Pro", serif;
    fill: var(--label-ink);
    text-anchor: middle;
  }
  .brand-name { font-size: 21px; letter-spacing: 1.5px; }
  .fragrance { font-size: 16px; }
  .back-title { font-size: 15px; }
  .back-copy { font-size: 10px; letter-spacing: 0.4px; }
  .brand-dot { fill: none; stroke: var(--label-ink); stroke-width: 1.4; }
</style>
</head>
<body>
<svg class="dieline" viewBox="0 0 1500 1250" xmlns="http://www.w3.org/2000/svg">
  <defs>
    <linearGradient id="woodTone" x1="0" y1="0" x2="0" y2="1">
      <stop offset="0" stop-color="var(--wood-light)"/>
      <stop offset="0.5" stop-color="var(--wood)"/>
      <stop offset="1" stop-color="var(--wood-dark)"/>
    </linearGradient>
    <linearGradient id="silverSheen" x1="0" y1="0" x2="1" y2="1">
      <stop offset="0" stop-color="var(--silver-mid)"/>
      <stop offset="0.35" stop-color="var(--silver-light)"/>
      <stop offset="0.7" stop-color="var(--silver-dark)"/>
      <stop offset="1" stop-color="var(--silver-light)"/>
    </linearGradient>
  </defs>

  <g class="flaps">
    <polygon class="flap" role="img" aria-label="Dark wood grain texture" points="97,288 310,288 332,368 332,385 70,385 70,368"/>
    <polygon class="flap" role="img" aria-label="Dark wood grain texture" points="735,288 945,288 970,368 970,385 710,385 710,368"/>
    <polygon class="flap" role="img" aria-label="Dark wood grain texture" points="70,705 332,705 332,720 310,800 97,800 70,720"/>
    <polygon class="flap" role="img" aria-label="Dark wood grain texture" points="710,705 970,705 970,720 945,800 735,800 710,720"/>
    <polygon class="flap" role="img" aria-label="Dark wood grain texture" points="335,885 705,885 705,900 675,985 365,985 335,900"/>
    <polygon class="flap" role="img" aria-label="Dark wood grain texture" points="990,48 1330,48 1345,100 1345,120 972,120 972,100"/>
    <polygon class="flap" role="img" aria-label="Dark wood grain texture" points="1345,390 1395,390 1420,420 1420,660 1395,690 1345,690"/>
  </g>

  <g class="foil">
    <rect class="silver-band" x="72" y="385" width="1273" height="320"/>
    <rect class="silver-band" x="335" y="700" width="370" height="185"/>
    <rect class="silver-band" x="972" y="120" width="373" height="270"/>
  </g>

  <g class="faces">
    <rect class="wood-face side-left" role="img" aria-label="Dark wood grain texture" x="90" y="403" width="228" height="283"/>
    <rect class="wood-face front" role="img" aria-label="Dark wood grain texture" x="350" y="403" width="340" height="283"/>
    <rect class="wood-face side-right" role="img" aria-label="Dark wood grain texture" x="725" y="403" width="230" height="283"/>
    <rect class="wood-face back" role="img" aria-label="Dark wood grain texture" x="990" y="403" width="338" height="283"/>
    <rect class="wood-face base" role="img" aria-label="Dark wood grain texture" x="352" y="705" width="338" height="163"/>
    <rect class="wood-face lid" role="img" aria-label="Dark wood grain texture" x="990" y="138" width="338" height="229"/>
  </g>

  <g class="front-label">
    <rect class="label-frame" x="385" y="443" width="267" height="193"/>
    <rect class="label-frame" x="391" y="449" width="255" height="181"/>
    <rect class="label-corner" x="385" y="443" width="10" height="10"/>
    <rect class="label-corner" x="642" y="443" width="10" height="10"/>
    <rect class="label-corner" x="385" y="626" width="10" height="10"/>
    <rect class="label-corner" x="642" y="626" width="10" height="10"/>
    <circle class="brand-dot" cx="518.5" cy="510" r="14"/>
    <text class="brand-name" x="518.5" y="566">Harbor Emberlight</text>
    <text class="fragrance" x="518.5" y="602">Sea Fern</text>
    <text class="fragrance" x="518.5" y="622">Driftwood Tide</text>
  </g>

  <g class="back-label">
    <rect class="label-frame" x="1030" y="445" width="257" height="203"/>
    <rect class="label-frame" x="1036" y="451" width="245" height="191"/>
    <rect class="label-corner" x="1030" y="445" width="10" height="10"/>
    <rect class="label-corner" x="1277" y="445" width="10" height="10"/>
    <rect class="label-corner" x="1030" y="638" width="10" height="10"/>
    <rect class="label-corner" x="1277" y="638" width="10" height="10"/>
    <text class="back-title" x="1158.5" y="473">Sea Fern</text>
    <text class="back-title" x="1158.5" y="493">Driftwood Tide</text>
    <line class="label-rule" x1="1088" y1="502" x2="1229" y2="502"/>
    <text class="back-copy" x="1158.5" y="521">Hand poured soy wax</text>
    <text class="back-copy" x="1158.5" y="536">with a crackling wooden wick</text>
    <text class="back-copy" x="1158.5" y="551">Burn for two hours at a time</text>
    <text class="back-copy" x="1158.5" y="566">trim wick to five millimetres</text>
    <text class="back-copy" x="1158.5" y="581">keep away from drafts</text>
    <text class="back-copy" x="1158.5" y="596">never leave a burning candle</text>
    <text class="back-copy" x="1158.5" y="611">unattended or near children</text>
    <text class="back-copy" x="1158.5" y="626">net weight 380 g</text>
  </g>
</svg>
</body>
</html>
```